New shirt company looking for a fun and edgy online retail website design

We're a new company looking for a simple yet attractive website to sell shirts/tops to a mostly younger female audience. Our name is Tavi Shirt Co. and the PlanHerd logo is uploaded. We're thinking a home page, three separate pages for our shirt "collections", and a contact page/cart page for a grand total of 5 pages. We'd like the website to be coded, easy for the consumer to navigate/shop/checkout, and easy to link to various social media platforms and online websites. For colors, we're aiming for various blues, light grey, and maybe tan/khaki. Our goal is to launch with approximately 20-30 tops/shirts (or 7-10) per page. Please let us know if you have any questions and thank you for helping us! We are very excited to see what is created!

Target Market(s)

Female teens to early twenties

Coding

Coded - Design and coding required

Number of Pages Required

3 page

Font styles to use
Decorative
Script

Colors
cee9f5
85cae6
33a6d7
0393ce
cfdfed
85acd3

Requirements
Must have
• Online shopping/purchasing capabilities, dropdowns to select sizes for each item, easy to add/remove new or seasoned items.

```html
<!DOCTYPE html>
<html lang="en">
<head>
<meta charset="utf-8">
<title>Tavi Shirt Co. — Home</title>
<link rel="stylesheet" href="https://fonts.googleapis.com/css2?family=Poppins:wght@300;400;500;600;800&display=swap">
<style>
:root{
  --navy:#003f97;
  --blue:#0055a5;
  --sky:#87cde8;
  --teal-light:#c6f1ee;
  --teal:#84d3cf;
  --ink:#222;
  --text:#333;
  --muted:#777;
  --line:#cfcfcf;
  --panel:#f5f5f5;
  --white:#fff;
  --canvas:#f1f1f1;
  --badge:#e32626;
}
*{box-sizing:border-box;margin:0;padding:0}
html,body{width:1200px;height:2400px;overflow:hidden;background:var(--canvas);font-family:'Poppins',sans-serif;color:var(--text)}
.page{position:absolute;left:164px;top:0;width:864px;height:2381px;background:var(--white);transform:scale(1.008);transform-origin:top left;overflow:hidden}
/* header */
.social{position:absolute;top:25px;width:30px;height:30px;border:1px solid var(--line);border-radius:2px;font-size:7px;font-weight:600;color:var(--navy);display:flex;align-items:center;justify-content:center}
.brand{position:absolute;left:396px;top:10px;width:72px;height:60px;background:var(--sky);display:flex;align-items:center;justify-content:center;font-size:12px;font-weight:500;color:var(--navy)}
.search{position:absolute;left:525px;top:26px;width:198px;height:29px;border:1px solid var(--line);border-radius:2px;font-size:9px;color:#999;padding:8px 14px}
.search svg{position:absolute;right:12px;top:8px}
.cart{position:absolute;left:736px;top:31px}
.cart-count{position:absolute;left:748px;top:29px;width:9px;height:9px;border-radius:50%;background:var(--badge);color:#fff;font-size:6px;text-align:center;line-height:9px}
/* nav */
.nav{position:absolute;left:0;top:80px;width:864px;height:53px;background:var(--navy);display:flex;justify-content:center;align-items:center;gap:22px}
.nav a{color:#fff;font-size:8.5px;font-weight:500;text-decoration:none;letter-spacing:.2px}
/* hero */
.hero{position:absolute;left:0;top:133px;width:864px;height:383px;background:linear-gradient(110deg,var(--teal-light) 0%,#a9e4df 55%,var(--teal) 100%)}
.hero-kicker{position:absolute;left:106px;top:93px;font-size:15px;font-weight:300;color:var(--ink)}
.hero-title{position:absolute;left:104px;top:118px;font-size:60px;font-weight:800;line-height:58px;color:var(--navy);letter-spacing:.5px}
.btn-solid{position:absolute;background:var(--navy);color:#fff;font-size:11px;display:flex;align-items:center;justify-content:center}
.hero-photo{position:absolute;left:440px;top:0;width:424px;height:383px;background:radial-gradient(ellipse at 60% 60%,#e8b98c 0%,#dcae84 30%,rgba(220,174,132,0) 60%)}
/* features */
.features{position:absolute;left:0;top:516px;width:864px;height:176px;background:var(--panel)}
.feature{position:absolute;top:44px;width:200px;text-align:center}
.feature .icon{height:40px;display:flex;align-items:center;justify-content:center}
.feature h3{font-size:10px;font-weight:500;color:var(--ink);margin-top:16px;line-height:14px}
.feature p{font-size:7.5px;color:var(--muted);margin-top:2px}
/* products */
.section-title{position:absolute;left:0;width:864px;top:756px;text-align:center;font-size:20px;font-weight:600;color:var(--text);letter-spacing:.5px}
.card{position:absolute;width:150px;text-align:center}
.card .photo{width:150px;height:195px}
.card .name{margin-top:28px;font-size:13px;color:var(--muted)}
.card .price{font-size:19px;font-weight:500;color:var(--ink);line-height:24px}
.card .buy{margin:10px auto 0;width:92px;height:34px;border:1px solid #555;font-size:11px;color:var(--ink);display:flex;align-items:center;justify-content:center}
.card .buy.active{background:var(--navy);border-color:var(--navy);color:#fff}
.see-all{position:absolute;left:370px;top:1896px;width:127px;height:37px;background:var(--blue);color:#fff;font-size:11px;font-weight:500;display:flex;align-items:center;justify-content:center}
/* newsletter */
.newsletter{position:absolute;left:0;top:2019px;width:864px;height:105px;background:var(--navy)}
.newsletter h2{position:absolute;left:187px;top:41px;font-size:17px;font-weight:400;color:#fff}
.news-input{position:absolute;left:315px;top:36px;width:264px;height:33px;background:#fff;font-size:7px;color:#aaa;padding:12px 13px}
.news-btn{position:absolute;left:579px;top:36px;width:97px;height:33px;border:1px solid #fff;background:var(--blue);color:#fff;font-size:8.5px;font-weight:500;display:flex;align-items:center;justify-content:center}
/* footer */
.footer{position:absolute;left:0;top:2124px;width:864px;height:257px;background:var(--panel)}
.fcol{position:absolute;top:46px}
.fcol h4{font-size:10.5px;font-weight:600;color:var(--ink);margin-bottom:12px}
.fcol li{list-style:none;font-size:7.5px;color:var(--muted);line-height:19.5px;padding-left:4px}
.fcol .addr{font-size:6.5px;color:var(--muted);line-height:8px;margin-bottom:8px;padding-left:1px}
.fsocial{display:flex;gap:4px;margin-top:2px}
.fsocial span{width:13px;height:13px;background:var(--navy)}
.rule{position:absolute;left:106px;top:204px;width:656px;height:1px;background:var(--line)}
.copyright{position:absolute;left:106px;top:225px;font-size:7px;color:var(--muted)}
.payments{position:absolute;left:422px;top:221px;width:340px;display:flex;justify-content:space-between}
.pay{font-size:9px;font-weight:500;color:var(--muted)}
</style>
</head>
<body>
<div class="page">

  <span class="social" style="left:106px">Yap</span>
  <span class="social" style="left:143px">Pix</span>
  <span class="social" style="left:179px">Chirr</span>
  <span class="social" style="left:216px">Netly</span>
  <div class="brand">Tavi</div>
  <div class="search">Search...
    <svg width="12" height="12" viewBox="0 0 12 12" fill="none" stroke="#888" stroke-width="1.2"><circle cx="5" cy="5" r="3.8"/><path d="M8 8l3 3"/></svg>
  </div>
  <svg class="cart" width="18" height="16" viewBox="0 0 18 16" fill="none" stroke="#666" stroke-width="1.2"><path d="M1 1h3l2 9h9l2-6H5"/><circle cx="7" cy="13.5" r="1.3"/><circle cx="14" cy="13.5" r="1.3"/></svg>
  <span class="cart-count">0</span>

  <nav class="nav">
    <a>HOME</a><a>COLLECTION ⌄</a><a>COLLECTION ⌄</a><a>BLOGS ⌄</a><a>CONTACT US ⌄</a>
  </nav>

  <section class="hero">
    <div class="hero-photo" role="img" aria-label="Two models in tan wrap dresses posing together"></div>
    <p class="hero-kicker">IT'S THE BEST TIME OF THE YEAR!</p>
    <h1 class="hero-title">GET UP TO<br>70% OFF</h1>
    <div class="btn-solid" style="left:106px;top:267px;width:110px;height:37px">SHOP NOW</div>
  </section>

  <section class="features">
    <div class="feature" style="left:111px">
      <div class="icon"><svg width="48" height="34" viewBox="0 0 48 34" fill="none" stroke="#222" stroke-width="1.4"><path d="M2 4h28v22H2zM30 12h9l7 8v6H30"/><circle cx="10" cy="28" r="3.5" fill="#f5f5f5"/><circle cx="38" cy="28" r="3.5" fill="#f5f5f5"/><path d="M10 15l4 4 8-8"/></svg></div>
      <h3>FREE SHIPPING</h3><p>Shipping on order over $99</p>
    </div>
    <div class="feature" style="left:334px">
      <div class="icon"><svg width="42" height="36" viewBox="0 0 42 36" fill="none" stroke="#222" stroke-width="1.4"><path d="M4 20l18-14 6 16-18 4zM10 25l3 8h4l-2-8M30 8l5-4M32 14h6M30 20l5 3"/></svg></div>
      <h3>FESTIVAL OFFER</h3><p>New Online Special Festival Offer</p>
    </div>
    <div class="feature" style="left:558px">
      <div class="icon"><svg width="40" height="38" viewBox="0 0 40 38" fill="none" stroke="#222" stroke-width="1.4"><circle cx="22" cy="17" r="14"/><path d="M5 12c-3 6 0 14 9 20l5-4-4-5-3 2c-2-3-3-6-2-9l3-1-2-6z"/><text x="22" y="20" font-size="7" font-family="Poppins,sans-serif" text-anchor="middle" fill="#222" stroke="none">24/7</text></svg></div>
      <h3>24 X 7 SERVICE</h3><p>Flexible service for user</p>
    </div>
  </section>

  <h2 class="section-title">LATEST PRODUCTS</h2>

  <div class="card" style="left:106px;top:820px"><div class="photo" role="img" aria-label="Model in black long-sleeve blouse" style="background:linear-gradient(180deg,#d9a884 0%,#d9a884 35%,#2a2a2a 36%,#1b1b1b 100%)"></div><p class="name">Product Name</p><p class="price">$120</p><div class="buy">SHOP NOW</div></div>
  <div class="card" style="left:275px;top:820px"><div class="photo" role="img" aria-label="Model in red button blouse" style="background:linear-gradient(180deg,#ececec 0%,#ececec 30%,#d8232f 31%,#c81e2a 90%,#222 91%)"></div><p class="name">Product Name</p><p class="price">$120</p><div class="buy active">SHOP NOW</div></div>
  <div class="card" style="left:444px;top:820px"><div class="photo" role="img" aria-label="Model in red puff-sleeve top and jeans" style="background:linear-gradient(180deg,#ededed 0%,#ededed 28%,#c8202b 29%,#b51c26 58%,#5b7fb3 59%,#4a6fa3 100%)"></div><p class="name">Product Name</p><p class="price">$120</p><div class="buy">SHOP NOW</div></div>
  <div class="card" style="left:612px;top:820px"><div class="photo" role="img" aria-label="Model in burgundy peplum top" style="background:linear-gradient(180deg,#f6f6f6 0%,#f6f6f6 26%,#8e1b22 27%,#7a161c 88%,#2d3f5c 89%)"></div><p class="name">Product Name</p><p class="price">$120</p><div class="buy">SHOP NOW</div></div>

  <div class="card" style="left:106px;top:1170px"><div class="photo" role="img" aria-label="Model in black bell-sleeve tunic" style="background:linear-gradient(180deg,#ececec 0%,#ececec 26%,#1c1c1c 27%,#151515 100%)"></div><p class="name">Product Name</p><p class="price">$120</p><div class="buy">SHOP NOW</div></div>
  <div class="card" style="left:275px;top:1170px"><div class="photo" role="img" aria-label="Model in gingham ruched-sleeve top" style="background:linear-gradient(180deg,#f3f3f3 0%,#f3f3f3 25%,#9a9aa2 26%,#7f8089 78%,#4a6590 79%)"></div><p class="name">Product Name</p><p class="price">$120</p><div class="buy">SHOP NOW</div></div>
  <div class="card" style="left:444px;top:1170px"><div class="photo" role="img" aria-label="Model in black and white leaf print tank" style="background:linear-gradient(180deg,#e9e9e9 0%,#e9e9e9 30%,#6b6b6b 31%,#3a3a3a 100%)"></div><p class="name">Product Name</p><p class="price">$120</p><div class="buy">SHOP NOW</div></div>
  <div class="card" style="left:612px;top:1170px"><div class="photo" role="img" aria-label="Model in black oversized blouse" style="background:linear-gradient(180deg,#ebebeb 0%,#ebebeb 28%,#1a1a1a 29%,#141414 82%,#4a6590 83%)"></div><p class="name">Product Name</p><p class="price">$120</p><div class="buy">SHOP NOW</div></div>

  <div class="card" style="left:106px;top:1522px"><div class="photo" role="img" aria-label="Black and white striped tee on hanger" style="background:radial-gradient(ellipse at 50% 45%,#8a8a8a 0%,#b9b9b9 35%,#f1f1f1 55%)"></div><p class="name">Product Name</p><p class="price">$120</p><div class="buy">SHOP NOW</div></div>
  <div class="card" style="left:275px;top:1522px"><div class="photo" role="img" aria-label="Burgundy bow-cuff blouse on hanger" style="background:radial-gradient(ellipse at 50% 45%,#7f1b2a 0%,#a0485a 35%,#f1f1f1 58%)"></div><p class="name">Product Name</p><p class="price">$120</p><div class="buy">SHOP NOW</div></div>
  <div class="card" style="left:444px;top:1522px"><div class="photo" role="img" aria-label="Gingham ruffle-hem tank on hanger" style="background:radial-gradient(ellipse at 50% 50%,#6d6d6d 0%,#a8a8a8 35%,#f1f1f1 58%)"></div><p class="name">Product Name</p><p class="price">$120</p><div class="buy">SHOP NOW</div></div>
  <div class="card" style="left:612px;top:1522px"><div class="photo" role="img" aria-label="Mustard off-shoulder top on hanger" style="background:radial-gradient(ellipse at 50% 45%,#e3ae22 0%,#eccb6e 30%,#f1f1f1 52%)"></div><p class="name">Product Name</p><p class="price">$120</p><div class="buy">SHOP NOW</div></div>

  <div class="see-all">See All Products</div>

  <section class="newsletter">
    <h2>NEWSLETTER</h2>
    <div class="news-input">Enter your Email</div>
    <div class="news-btn">SIGN UP</div>
  </section>

  <footer class="footer">
    <div class="fcol" style="left:101px"><h4>QUICK LINKS</h4><ul><li>Contact Us</li><li>About Us</li><li>Dive Equipment Insurance</li><li>Dive Travel Insurance</li><li>Visit Us In Store</li><li>Careers</li></ul></div>
    <div class="fcol" style="left:270px"><h4>USEFUL LINKS</h4><ul><li>Affiliate Opportunities</li><li>Delivery</li><li>Returns</li><li>Privacy</li><li>Terms &amp; Conditions</li><li>Wholesale</li></ul></div>
    <div class="fcol" style="left:441px"><h4>ALL PRODUCTS</h4><ul><li>Products</li><li>Packages</li><li>Servicing</li><li>Liveaboard Offers</li><li>Superyacht Services</li><li>Scuba Diving Insurance</li></ul></div>
    <div class="fcol" style="left:607px"><h4>CONTACT US</h4>
      <p class="addr">Monday-Friday: 7am to 5pm<br>Dispatch: 24 / 7</p>
      <p class="addr">4100 Harbor Lane Ave<br>Millport, NJ 08810</p>
      <p class="addr">210 Coral 6th Court,<br>Palm Shore, FL 33400</p>
      <div class="fsocial"><span></span><span></span><span></span><span></span></div>
    </div>
    <div class="rule"></div>
    <p class="copyright">Copyright © 2020 Company Name</p>
    <div class="payments">
      <span class="pay">Kestra</span>
      <span class="pay">Lumo</span>
      <span class="pay">Brisk</span>
      <span class="pay">Norra</span>
      <span class="pay">Quill</span>
      <span class="pay">Fenwick</span>
    </div>
  </footer>
</div>
</body>
</html>
```